Company Mission & Values Poster

I'd like an A2 Portrait Poster displaying our company's Mission & Values.
See our website for our logo, fonts, mission & values.
https://valtemo.com.au/

Our Mission: Creating homes for abundant life
Values: Love, Thinking, Team, Zoe.

Some ideas to consider:
Mission as the Headline then
A logo for each of the 4 Values and the words

Target Market(s)

Myself & my team

Industry/Entity Type

Real Estate

Font styles to use
Other font styles liked:
• Company fonts as seen on our website

```html
<!DOCTYPE html>
<html lang="en">
<head>
<meta charset="utf-8">
<title>Valtemo – Mission &amp; Values</title>
<link rel="stylesheet" href="https://fonts.googleapis.com/css2?family=Gloock&family=Plus+Jakarta+Sans:wght@400;500;800&display=swap">
<style>
  :root {
    --hero-green: #2c4f42;
    --hero-deep: #1f3d33;
    --values-bg: #0e3a33;
    --card-bg: #1b6358;
    --badge-bg: #0f443c;
    --badge-ring: #2a7a6d;
    --rule: #4f9f91;
    --white: #ffffff;
    --card-text: #d7ece7;
    --footer-bg: #f3f5f4;
    --brand-ink: #0f3a33;
  }
  * { margin: 0; padding: 0; box-sizing: border-box; }
  html, body { width: 840px; height: 1200px; overflow: hidden; background: var(--values-bg); }
  .poster { position: relative; width: 840px; height: 1200px; overflow: hidden; }

  .hero { position: absolute; inset: 0 0 auto 0; height: 420px; }
  .hero-photo {
    position: absolute; inset: 0;
    background:
      radial-gradient(ellipse at 85% 30%, rgba(80,110,90,.55), transparent 55%),
      radial-gradient(ellipse at 15% 70%, rgba(60,90,70,.5), transparent 60%),
      linear-gradient(180deg, #3a5b4d 0%, var(--hero-green) 45%, var(--hero-deep) 100%);
  }
  .hero-content { position: relative; text-align: center; color: var(--white); }
  .headline {
    font-family: "Gloock", serif; font-weight: 400;
    font-size: 70px; line-height: 72px; letter-spacing: 1px;
    padding-top: 36px;
  }
  .section-title {
    font-family: "Plus Jakarta Sans", sans-serif; font-weight: 800;
    font-size: 44px; letter-spacing: .5px; line-height: 1;
  }
  .hero .section-title { margin-top: 30px; }
  .mission-text {
    font-family: "Plus Jakarta Sans", sans-serif; font-weight: 500;
    font-size: 19px; line-height: 25.5px; margin-top: 16px;
  }

  .values {
    position: absolute; top: 420px; left: 0; right: 0; height: 658px;
    background: var(--values-bg); color: var(--white); text-align: center;
  }
  .values .section-title { margin-top: 44px; }
  .values-intro {
    font-family: "Gloock", serif; font-size: 32px; line-height: 40.5px;
    margin-top: 14px; letter-spacing: .3px;
  }

  .value-cards { position: absolute; top: 308px; left: 32px; right: 28px; display: flex; gap: 20px; }
  .value-card {
    position: relative; width: 180px; height: 320px;
    background: var(--card-bg); border-radius: 4px 4px 16px 16px;
  }
  .value-badge {
    position: absolute; left: 50%; top: -55px; transform: translateX(-50%);
    width: 110px; height: 110px; border-radius: 50%;
    background: var(--badge-bg); border: 3px solid var(--badge-ring);
    display: flex; align-items: center; justify-content: center;
  }
  .value-badge svg { width: 48px; height: 48px; fill: none; stroke: var(--white); stroke-width: 2; stroke-linecap: round; stroke-linejoin: round; }
  .value-name {
    font-family: "Gloock", serif; font-size: 35px; line-height: 1;
    margin: 78px auto 0; width: 150px; padding-bottom: 8px;
    border-bottom: 1.5px solid var(--rule);
  }
  .value-card.zoe .value-name { margin-top: 85px; }
  .value-text {
    font-family: "Plus Jakarta Sans", sans-serif; font-weight: 400;
    font-size: 13.5px; line-height: 17px; color: var(--card-text);
    padding: 10px 12px 0;
  }

  .footer {
    position: absolute; left: 0; right: 0; bottom: 0; height: 122px;
    background: var(--footer-bg);
    display: flex; align-items: center; justify-content: center; gap: 14px;
  }
  .brand-dot { width: 30px; height: 30px; border-radius: 50%; background: var(--brand-ink); }
  .brand-name {
    font-family: "Gloock", serif; font-size: 52px; letter-spacing: 8px;
    color: var(--brand-ink); line-height: 1;
  }
</style>
</head>
<body>
<main class="poster">
  <section class="hero">
    <div class="hero-photo" role="img" aria-label="Photograph of a modern apartment building surrounded by lush garden greenery, tinted green"></div>
    <div class="hero-content">
      <h1 class="headline">Creating homes for<br>abundant life</h1>
      <h2 class="section-title">OUR MISSION</h2>
      <p class="mission-text">We wholeheartedly believe that home is an extraordinary place:<br>A haven where life unfolds in all its glory.<br>Where we find solace, make cherished memories with loved ones,<br>and savour the&nbsp; natural beauty that surrounds us.</p>
    </div>
  </section>

  <section class="values">
    <h2 class="section-title">OUR VALUES</h2>
    <p class="values-intro">We believe business can be a force for good.<br>Our values shape the way we work,<br>and how we make decisions.</p>

    <div class="value-cards">
      <article class="value-card love">
        <div class="value-badge">
          <svg viewBox="0 0 48 48"><path d="M20 36 C10 29 4 23 5 16 c1-6 9-8 13-2 c3-5 10-5 12 0"/><path d="M30 38 c-8-6-13-11-12-17 c1-6 9-7 12-2 c3-5 11-4 12 2 c1 6-5 11-12 17z"/></svg>
        </div>
        <h3 class="value-name">Love</h3>
        <p class="value-text">Our mission is founded in our love and respect for people - those we develop for, those in our teams and those in the communities we create and operatewithin.</p>
      </article>

      <article class="value-card thinking">
        <div class="value-badge">
          <svg viewBox="0 0 48 48"><path d="M16 42 v-7 c-5-3-8-8-7-14 c1-8 8-13 16-12 c8 1 13 7 12 14 l3 6 h-3 v5 c0 2-2 3-4 3 h-4 v5"/><circle cx="24" cy="20" r="5"/><path d="M22 25 v3 h4 v-3 M24 10 v3 M15 19 h3 M30 19 h3 M17 13 l2 2 M31 13 l-2 2"/></svg>
        </div>
        <h3 class="value-name">Thinking</h3>
        <p class="value-text">We believe in the power of thinking. Our rigorous and creative processes create beautifully considered solutions for our purchasers, the communities we develop within and the environment.</p>
      </article>

      <article class="value-card team">
        <div class="value-badge">
          <svg viewBox="0 0 48 48"><circle cx="13" cy="15" r="4.5"/><circle cx="24" cy="13" r="5"/><circle cx="35" cy="15" r="4.5"/><path d="M4 34 c0-7 4-11 9-11 c3 0 5 1 6 3"/><path d="M44 34 c0-7-4-11-9-11 c-3 0-5 1-6 3"/><path d="M13 38 c0-8 5-13 11-13 s11 5 11 13"/></svg>
        </div>
        <h3 class="value-name">Team</h3>
        <p class="value-text">Property development is a team sport. We surround ourselves with the best designers and advisers. We strive to create an environment that allows them to do their best work and love doing it.</p>
      </article>

      <article class="value-card zoe">
        <div class="value-badge">
          <svg viewBox="0 0 48 48"><path d="M30 8 A17 17 0 1 0 41 22"/><path d="M30 8 l-5 -2 M30 8 l-2 5"/><path d="M24 31 c-5-4-8-7-7-10 c1-3 5-3 7 0 c2-3 6-3 7 0 c1 3-2 6-7 10z"/><path d="M12 24 h7 l2-3 l3 6 l2-3 h9"/></svg>
        </div>
        <h3 class="value-name">Zoe</h3>
        <p class="value-text">Our mission is to create places for ‘Zoe’ - the Greek word for abundant life. We do this through exquisite design, quality construction and celebrating nature.</p>
      </article>
    </div>
  </section>

  <footer class="footer">
    <span class="brand-dot" aria-hidden="true"></span>
    <span class="brand-name">VALTEMO</span>
  </footer>
</main>
</body>
</html>
```